Tourism Marketing needing sleek, clear design for business card & proposal documents.

***Company background***
"Quiet Harbour" is a company specializing in tourism marketing and project management. We do international wholesale, event management as well as ongoing representation of tourism and hospitality companies.

***Target market***
We cater to tourism companies and hotel professionals.

***Task***
We would like to get a single sided business card designed (but will still consider two sided, we are open to any ideas you may have). The layout for this card should be modern and elegant. Currently we do not have a logo, but we would like our business name in a really simple typography for the business card (similar to Moonrise Palace's logo - www.moonrisepalace-example.com.au).We are after a design that is clear, strong enough to be recognised as Quiet Harbour that does not require any fancy design. Another option is a simple play on QH (Quiet Harbour) or simply have Quiet Harbour featured elsewhere on card more as a brand/logo.

Feel free to submit different fonts if you feel you have any other fonts/designs that may be suitable for this card other than sans serifs. Should this project be successful, we will be considering several other projects for business proposal templates and eventually a website design.

The information that needs to go on the card are as follows:

Marta Holloway
Director
Quiet Harbour
Tourism Marketing & Representation
87 Wendover Parade
Prahran, Victoria, 3181 Australia
T +61 498203617 E marta@quietharbour-example.com.au

***Look and feel***
We'd like the business card design to express the following:
Modern, sleek, elegant, simple, discreet, quality, subtle, professional, creative, innovation

In terms of typography, we like something really simple and blocky (similar font to Moonrise Palace's logo - www.moonrisepalace-example.com.au)

***Colour scheme***
Shades of grey and dark teal

***Note***
Although our main target market are professionals, we would like the business card design to be versatile enough to be used outside of the tourism industry and need to appeal to different markets.

I do not have existing logo. Was hoping for a design that may be clear, strong enough not to require one. Other option is a simple play on QH (Quiet Harbour) or simply have Quiet Harbour featured elsewhere on card more as a brand/logo.

Marta Holloway
Director
Quiet Harbour Pty Ltd 
87 Wendover Parade
T +61 498203617  E  marta@quietharbour-example.com.au

Thank you for designs so far. Many have used a mauve colour which matches our company profile. This is not necessary, as that is just a draft and will be completely redesigned, so dont  feel you need to incorporate the mauve.

My colour preferences are for a white or grey background, and I like fonts in dark teals, grey or other sophisticated but modern colours. feel free to submit different fonts if you you have other fonts you thing would be suitable for this card, along with sans serifs. Should this project be successful, we will be considering several others for business proposal templates and eventually website. 

Target Market(s)

International Hospitality Senior Executives, Directors of International Tourism Companies, Directors of Tourism Bodies Internationally, local Tourism

Industry/Entity Type

Hospitality

Requirements
Should not have
• must not have bright garish colour, swirly patterns or anything that dates too much.

```html
<!DOCTYPE html>
<html lang="en">
<head>
<meta charset="utf-8">
<title>Quiet Harbour — Business Card</title>
<link rel="stylesheet" href="https://fonts.googleapis.com/css2?family=PT+Sans:wght@400;700&display=swap">
<style>
  :root {
    --page-bg: #fdfdfd;
    --card-bg: #fcfcfc;
    --card-edge: #8a8a8a;
    --divider: #8c8c8c;
    --ink: #231f20;
    --teal: #1c9db1;
    --teal-soft: #4aa9bd;
    --shadow: rgba(0, 0, 0, 0.45);
  }
  * { margin: 0; padding: 0; box-sizing: border-box; }
  html, body {
    width: 1200px;
    height: 900px;
    overflow: hidden;
    background: var(--page-bg);
    font-family: "PT Sans", "Myriad Pro", Arial, sans-serif;
    color: var(--ink);
  }
  .canvas {
    position: relative;
    width: 1200px;
    height: 900px;
  }
  .business-card {
    position: absolute;
    left: 330px;
    top: 265px;
    width: 587px;
    height: 337px;
    background: var(--card-bg);
    border: 1px solid var(--card-edge);
    box-shadow: 4px 4px 4px var(--shadow);
  }
  .card-person {
    position: absolute;
    left: 23px;
    top: 20px;
  }
  .person-name {
    font-weight: 700;
    font-size: 26px;
    line-height: 1;
    letter-spacing: 0.2px;
    text-transform: uppercase;
  }
  .person-role {
    margin-top: 2px;
    font-size: 20px;
    line-height: 1.1;
    color: var(--teal-soft);
  }
  .card-divider {
    position: absolute;
    left: 0;
    right: 0;
    top: 162px;
    height: 2px;
    background: var(--divider);
  }
  .card-company {
    position: absolute;
    left: 0;
    right: 0;
    top: 186px;
    text-align: center;
  }
  .company-name {
    font-weight: 400;
    font-size: 37px;
    line-height: 1;
    letter-spacing: 0.5px;
    text-transform: uppercase;
    color: var(--ink);
  }
  .company-tagline {
    margin-top: 4px;
    font-size: 14.5px;
    line-height: 1.1;
    color: var(--teal);
  }
  .company-address {
    margin-top: 8px;
    font-size: 17px;
    line-height: 1.3;
  }
  .company-contact {
    margin-top: 8px;
    display: flex;
    justify-content: center;
    gap: 22px;
    font-size: 17px;
  }
  .contact-label {
    font-weight: 700;
    color: var(--teal);
    margin-right: 6px;
  }
</style>
</head>
<body>
  <main class="canvas">
    <article class="business-card">
      <header class="card-person">
        <h1 class="person-name">Marta Holloway</h1>
        <p class="person-role">Director</p>
      </header>

      <div class="card-divider"></div>

      <section class="card-company">
        <p class="company-name">Quiet Harbour</p>
        <p class="company-tagline">Tourism Marketing &amp; Representation</p>
        <address class="company-address" style="font-style: normal;">
          87 Wendover Parade Prahran,<br>
          Victoria, 3181 Australia
        </address>
        <p class="company-contact">
          <span><span class="contact-label">T</span>+61 498203617</span>
          <span><span class="contact-label">E</span>marta@quietharbour-example.com.au</span>
        </p>
      </section>
    </article>
  </main>
</body>
</html>
```